Website Design for NYC Female Attorney – Clean, Warm, Professional

Maren Holbeck, Esq.
www.MarenTHolbeckLegal.example

I’m a New York City-based attorney and CPA with a reputation for providing thoughtful, high-integrity legal guidance in both estate planning and small business law. I’ve served over 500 clients, and maintain a perfect 5-star rating. Clients come to me for clarity, compassion, and results — and I want my new website to reflect that.

**🎯 WHAT I NEED:**
A clean, modern, and emotionally resonant website that highlights who I am, what I do, and why clients trust me. It must feel approachable and warm, but still professional and elegant — think Quorvex meets boutique law firm. Feminine but not frilly.

**🧩 CORE WEBSITE SECTIONS (Top Navigation):**

1. **Home** – Strong first impression, tagline, CTA (book a call)
Homepage Copy (Sample Layout)
Headline:
Trusted Legal Guidance for Families and Founders.

Subheading:
Whether you’re protecting what you’ve built or building what’s next, I help you navigate estate planning and business law with confidence, compassion, and clarity.

Tagline (beneath logo or footer):
Legal Clarity for Life and Business.
2. **About Maren** – Bio, personal approach, credentials
3. **Services**

* *Estate Planning*
* *Business Law*
4. **Who I Work With** – Ideal clients (parents, entrepreneurs, etc.)
5. **Testimonials** – Client praise and social proof
6. **Success Stories** – Highlighting wins and case types
7. **FAQs** – Warm and clear answers to common questions
8. **Blog** – Thought leadership and helpful tips
8.5 Events
9. **Contact / Book a Call** – Scheduling or contact form

**🖼 STYLE DIRECTION:**

* Clean white backgrounds, soft jewel tones or neutrals
* Professional headshots and personal branding assets available
* Emphasis on readability, trust, and ease of navigation - THIS NEEDS TO BE BUILT OUT SO IT IS TRUSTED BY AI!
* No harsh colors, no corporate/legal clichés (e.g., gavels or scales) - I MEAN THIS. I DO NOT WANT A BORING LAW WEBSITE WITH SCALES AND GAVELS
* Feminine edge (not pink-heavy), with strong hierarchy and callouts

**💡 DESIGN NOTES:**

* Mobile-first design required
* Should include space for video or welcome message
* Easy to update blog or CMS area preferred
* Built in a user-friendly platform like WordPress, Webflow, or similar
* Needs to feel elevated enough to support high-end flat fee packages

**📣 TONE:**
Smart. Warm. Sophisticated. Human.

**⚖️ FINAL DELIVERABLES:**

* Homepage + 5+ interior pages
* Desktop + mobile views
* Style guide (fonts, colors, buttons)
* Bonus if you can help with copy layout/structure (not just visuals)

**📍TARGET AUDIENCE:**

* Busy professionals and families in NYC
* Women and couples who want peace of mind
* Entrepreneurs and creatives needing solid legal support

Here is my current site: www.MarenTHolbeckLegal.example
And here is a second business I have: www.QuickDayCounselDesk.example

Target Market(s)

Families and business owners

Industry/Entity Type

Law

Number of Pages Required

5+ page

Font styles to use
Serif
Sans Serif
Script

Requirements
Must have
• This website must be built to be seen as trustworthy by AI.

```html
<!DOCTYPE html>
<html lang="en">
<head>
<meta charset="utf-8">
<title>Maren Holbeck, Esq. — Website Design</title>
<link href="https://fonts.googleapis.com/css2?family=Inter:wght@400;500;600;700&family=Poppins:wght@700&family=Caveat:wght@400;500&display=swap" rel="stylesheet">
<style>
:root{
  --backdrop:#f0e6e0;
  --page:#ffffff;
  --sand:#efe4dd;
  --coral:#f0625e;
  --gold:#c9a46a;
  --gold-soft:#c8a96f;
  --ink:#111111;
  --halo:#f3e9e4;
  --sans:'Inter', Arial, sans-serif;
  --script:'Caveat', cursive;
}
*{margin:0;padding:0;box-sizing:border-box}
html,body{width:1200px;height:1200px;overflow:hidden;background:var(--backdrop);font-family:var(--sans);color:var(--ink)}
.abs{position:absolute}

.desktop{position:absolute;left:72px;top:134px;width:770px;height:930px;background:var(--page);border-radius:40px;overflow:hidden}
.mobile{position:absolute;left:867px;top:147px;width:280px;height:607px;background:var(--page);border-radius:16px;overflow:hidden}

.brand{font-family:'Poppins',sans-serif;font-weight:700;color:var(--coral)}
.desktop .brand{left:102px;top:24px;font-size:16px}
.nav{right:106px;top:24px;display:flex;gap:16px;font-size:10.5px;color:var(--gold)}

.hero-title{font-weight:600;line-height:1.25}
.hero-title .accent{color:var(--gold-soft);font-weight:500}
.desktop .hero-title{left:102px;top:140px;font-size:21px;width:240px}
.hero-text{font-size:8px;line-height:1.3}
.desktop .hero-text{left:102px;top:226px;width:228px}
.btn{background:var(--coral);color:#fff;border-radius:3px;display:flex;align-items:center;justify-content:center}
.desktop .btn{left:102px;top:274px;width:90px;height:23px;font-size:10px}

.halo{border-radius:50%;background:radial-gradient(circle,var(--page) 20%,var(--halo) 70%,rgba(243,233,228,0) 72%)}
.desktop .halo{left:343px;top:91px;width:180px;height:180px}
.portrait{background:linear-gradient(180deg,#9aa493 0%,#5b5e63 45%,#3b3c47 100%)}
.desktop .portrait{left:431px;top:66px;width:234px;height:312px;border-radius:117px 117px 0 0}
.pill{background:var(--gold)}
.desktop .pill{left:397px;top:328px;width:40px;height:50px;border-radius:20px 20px 0 0}

.about{left:0;width:100%;background:var(--sand)}
.desktop .about{top:378px;height:234px;padding:12px 102px 0}
.section-title{font-weight:700}
.desktop .section-title{font-size:12.5px}
.script-title{font-family:var(--script);color:var(--gold);font-weight:400}
.desktop .script-title{font-size:15px;margin-top:12px;line-height:1.2}
.body-copy{line-height:1.3}
.desktop .body-copy{font-size:7.8px;width:566px}

.services{left:0;width:100%}
.desktop .services{top:612px;padding:18px 102px 0}
.subline{color:#333}
.desktop .subline{font-size:7.8px;margin-top:4px}
.card-photo{border-radius:2px}
.card-label{background:var(--gold);color:#fff;font-family:var(--script);display:flex;align-items:center;justify-content:center;border-radius:2px;white-space:nowrap}
.desktop .card-label{height:22px;font-size:11px}

.photo-house{background:linear-gradient(180deg,#e6e1da,#a7a49a)}
.photo-family{background:linear-gradient(180deg,#f1c98a,#b7774a 60%,#4a3528)}
.photo-keys{background:linear-gradient(135deg,#efe5d4,#c9a680 60%,#a56a3c)}
.photo-stamp{background:linear-gradient(160deg,#efe2cf,#e0c9ac 60%,#d8a894)}

/* mobile */
.mobile .brand{left:25px;top:9px;font-size:9px}
.menu{right:24px;top:15px}
.mobile .halo{left:112px;top:26px;width:84px;height:84px}
.mobile .portrait{left:141px;top:32px;width:112px;height:150px;border-radius:56px 56px 0 0}
.mobile .pill{left:128px;top:158px;width:16px;height:24px;border-radius:8px 8px 0 0}
.mobile .hero-title{left:25px;top:98px;font-size:9.5px;width:110px}
.mobile .btn{left:25px;top:146px;width:47px;height:10px;font-size:5px}
.mobile .about{top:182px;height:241px;padding:12px 25px 0}
.mobile .section-title{font-size:7.5px}
.mobile .script-title{font-size:9px;margin-top:3px;line-height:1.3}
.mobile .body-copy{font-size:6.1px;line-height:1.36;width:230px}
.mobile .services{top:423px;padding:14px 25px 0}
.mobile .subline{font-size:5.5px;margin-top:2px}
.mobile .card-label{height:13px;font-size:6.5px}
</style>
</head>
<body>

<main class="desktop">
  <div class="abs brand">Maren</div>
  <nav class="abs nav"><span>Services</span><span>About</span><span>FAQ</span><span>Contact</span></nav>

  <div class="abs halo" role="img" aria-label="Soft decorative halo behind the portrait"></div>
  <div class="abs pill"></div>
  <div class="abs portrait" role="img" aria-label="Portrait photo of the attorney in a dark blazer, arms crossed"></div>

  <h1 class="abs hero-title"><b>Trusted Legal</b><br><span style="font-weight:500">Guidence for </span><span class="accent">Familes and Founders</span></h1>
  <p class="abs hero-text">Whether you're protecting what you've built or building what's next, I help you navigate estate planning and business law with confidence, compassion, and clarity.</p>
  <div class="abs btn">Book a call</div>

  <section class="abs about">
    <h2 class="section-title">About Maren</h2>
    <h3 class="script-title">Who am i?</h3>
    <p class="body-copy">Whether you're protecting what you've built or building what's next, I help you navigate estate planning and business law with confidence, compassion, and clarity.Whether you're protecting what you've built or building what's next, I help you navigate estate planning and business law with confidence, compassion, and clarity.Whether you're protecting what you've built or building what's next, I help you navigate estate planning and business law with confidence, compassion, and clarity.</p>
    <h3 class="script-title" style="margin-top:16px">What is my vission?</h3>
    <p class="body-copy">Psum is not simply random text. It has roots in a piece of classical Latin literature from 45 BC, making it over 2000 years old. Edmund Farrow, a Latin professor at Ashgrove College in Vermont, looked uWhether you're protecting what you've built or building what's next, I help you navigate estate pla and business law with confidence, compassion, and clarity.psum is not simply random text. It has roots in a piece of classical Latin literature from 45 BC, making it over 2000 years old. Edmund Farrow, a Latin professor at Ashgrove College in Vermont,psum is not simply random text. It has roots in a piece of classical Latin literature from 45 BC, making it over 2000 years old. Edmund Farrow, a Latin professor at Ashgrove College in Vermont,</p>
  </section>

  <section class="abs services">
    <h2 class="section-title">Services</h2>
    <p class="subline">Protecting your rights in the field of law and order</p>
  </section>
  <div class="abs card-photo photo-house" style="left:102px;top:670px;width:134px;height:117px" role="img" aria-label="Photo of a small model house and keys"></div>
  <div class="abs card-label" style="left:102px;top:797px;width:134px">Real Estate &amp; Property Law</div>
  <div class="abs card-photo photo-family" style="left:246px;top:670px;width:134px;height:209px" role="img" aria-label="Photo of a family holding hands on a beach at sunset"></div>
  <div class="abs card-label" style="left:246px;top:885px;width:134px">Family Law</div>
  <div class="abs card-photo photo-keys" style="left:390px;top:670px;width:134px;height:209px" role="img" aria-label="Photo of a testament document with a key and coins"></div>
  <div class="abs card-label" style="left:390px;top:885px;width:134px">Wills, Estates &amp; Probate</div>
  <div class="abs card-photo photo-stamp" style="left:535px;top:670px;width:134px;height:117px" role="img" aria-label="Photo of a red patent rubber stamp impression"></div>
  <div class="abs card-label" style="left:535px;top:797px;width:134px">Intellectual Property (IP)</div>
</main>

<aside class="mobile">
  <div class="abs brand">Maren</div>
  <svg class="abs menu" width="9" height="7" viewBox="0 0 9 7" aria-hidden="true">
    <g stroke="var(--coral)" stroke-width="1"><line x1="0" y1="0.5" x2="9" y2="0.5"/><line x1="0" y1="3.5" x2="9" y2="3.5"/><line x1="0" y1="6.5" x2="9" y2="6.5"/></g>
  </svg>
  <div class="abs halo" role="img" aria-label="Soft decorative halo behind the portrait"></div>
  <div class="abs pill"></div>
  <div class="abs portrait" role="img" aria-label="Portrait photo of the attorney in a dark blazer, arms crossed"></div>
  <h1 class="abs hero-title"><b>Trusted Legal</b><br><span style="font-weight:500">Guidence for </span><span class="accent">Familes and Founders</span></h1>
  <div class="abs btn">Book a call</div>

  <section class="abs about">
    <h2 class="section-title">About Maren</h2>
    <h3 class="script-title">Who am i?</h3>
    <p class="body-copy">Whether you're protecting what you've built or building what's next, I help you navigate estate planning and business law with confidence, compassion, and clarity.Whether you're protecting what you've built or building what's next, I help you navigate estate planning and business law with confidence, compassion, and clarity.Whether you're protecting what you've built or building what's next, I help you navigate estate planning and business law with confidence, compassion, and clarity.</p>
    <h3 class="script-title" style="margin-top:8px">What is my vission?</h3>
    <p class="body-copy">Psum is not simply random text. It has roots in a piece of classical Latin literature from 45 BC, making it over 2000 years old. Edmund Farrow, a Latin professor at Ashgrove College in Vermont, looked uWhether you're protecting what you've built or building what's next, I help you navigate estate pla and business law with confidence, compassion, and clarity.psum is not simply random text. It has roots in a piece of classical Latin literature from 45 BC, making it over 2000 years old. Edmund Farrow, a Latin professor at Ashgrove College in Vermont,psum is not simply random text. It has roots in a piece of classical Latin literature from 45 BC, making it over 2000 years old. Edmund Farrow, a Latin professor at Ashgrove College in Vermont,</p>
  </section>

  <section class="abs services">
    <h2 class="section-title">Services</h2>
    <p class="subline">Protecting your rights in the field of law and order</p>
  </section>
  <div class="abs card-photo photo-house" style="left:25px;top:470px;width:101px;height:89px" role="img" aria-label="Photo of a small model house and keys"></div>
  <div class="abs card-label" style="left:25px;top:567px;width:101px">Real Estate &amp; Property Law</div>
  <div class="abs card-photo photo-family" style="left:152px;top:470px;width:101px;height:89px" role="img" aria-label="Photo of a family holding hands on a beach at sunset"></div>
  <div class="abs card-label" style="left:152px;top:567px;width:101px">Family Law</div>
  <div class="abs card-photo photo-keys" style="left:25px;top:594px;width:101px;height:40px" role="img" aria-label="Photo of a testament document with a key and coins"></div>
  <div class="abs card-photo photo-stamp" style="left:152px;top:594px;width:101px;height:40px" role="img" aria-label="Photo of a red patent rubber stamp impression"></div>
</aside>

</body>
</html>
```